Tech company needs a brochure design

Hi there.

We have written the text for a 4 page brochure, and this needs laying out.

We are in the process of rebranding, and have a new logo, but haven't yet established a colour pallete or design style.

Our current preference is for simple and bold. An example is the current website holding page is halcyra.io

Colour pallet should pull from the logo for primary colours, but we're open to secondary colours.

The layout in the document is not set in stone, but should be used as a guideline.

The final text is almost ready (we're polishing the phrasing), but it will be almost identical in the number of words and layout.

Target Market(s)

Typically, they are companies that operate in highly regulated industries, such as Financial Services, Telecoms or Healthcare, are data-centric and need to adhere to regulations such as GDPR. Or, data-sensitive, such as Legal, Accountancy or even Retail, where a breach of the network would give access to highly sensitive information.

Regulations and compliance requirements affect the systems they have in place, particularly when it comes to managing and securing data.

All of this impacts the IT infrastructure that is needed, and Halcyra can provide a seamless network that allows for all the regulations and doesn’t affect the working environment.

Halcyra sells into these environments at a senior level – IT Director, CIO, CTO.

Industry/Entity Type

Cyber Security

Font styles to use
Sans Serif
Other font styles liked:
• Nexa

Requirements
Must have
• 4 pages in landscape
Clean design
Be appropriate for corporate/business environments but still have vitality
use attached logo for colours - Gray is #2f2f2f
Nice to have
• Can be white or dark based
Should not have
• Not Fussy
Icons that don’t have any relevance

```html
<!DOCTYPE html>
<html lang="en">
<head>
<meta charset="utf-8">
<title>Halcyra Brochure Spreads</title>
<link href="https://fonts.googleapis.com/css2?family=Montserrat:wght@600;700;800&family=Open+Sans:wght@400;600;700&display=swap" rel="stylesheet">
<style>
:root{
  --orange:#e2531a;
  --orange-deep:#d9480f;
  --graphite:#2f2f2f;
  --dark-page:#3a3a3a;
  --stage:#1f1f1f;
  --paper:#ffffff;
  --mist:#ececec;
  --mist-deep:#d9d9d9;
  --rule:#9a9a9a;
  --text:#3b3b3b;
}
*{box-sizing:border-box;margin:0;padding:0}
html,body{width:978px;height:1200px;overflow:hidden}
body{background:var(--stage);position:relative;font-family:"Open Sans",Arial,sans-serif;color:var(--text)}
.page{position:absolute;width:358px;height:254px;overflow:hidden;background:var(--paper)}
.abs{position:absolute}
.heading{font-family:"Montserrat",Arial,sans-serif;font-weight:800;text-transform:uppercase;letter-spacing:1.2px;line-height:1.2}
.body-copy{font-size:4.2px;line-height:1.55;text-align:justify}
.body-copy p+p{margin-top:3px}
.wordmark{font-family:"Montserrat",Arial,sans-serif;font-weight:600;color:var(--graphite);letter-spacing:-.2px}
.photo{position:absolute}

/* cover */
.cover{left:338px;top:44px}
.cover .wordmark{left:18px;top:27px;font-size:17px}
.cover .url-tag{left:263px;top:26px;width:81px;height:17px;background:var(--orange);color:#fff;font-size:6px;font-weight:700;display:flex;align-items:center;justify-content:center}
.cover .hero{left:18px;top:65px;width:324px;height:103px;background:radial-gradient(circle at 72% 45%,#cfe8ff 0,#3a8de0 8%,#123a7a 30%,#0a1530 60%,#05070f 100%)}
.cover .headline{left:0;width:358px;top:150px;text-align:center;font-size:15.5px;letter-spacing:.2px}
.cover .headline span{display:block;line-height:1.06}
.cover .l1{color:#fff}
.cover .l2{color:var(--orange)}
.cover .l3{color:var(--graphite)}
.cover .cover-rule{left:0;top:204px;width:358px;height:1px;background:var(--mist-deep)}
.cover .tagline{right:16px;top:224px;font-size:6.5px;color:var(--orange)}

/* provider spread */
.provider{left:135px;top:325px;background:linear-gradient(120deg,#f4f4f4,#e4e4e4)}
.provider .title{left:24px;top:28px;font-size:11px;line-height:1.3}
.provider .title .o{color:var(--orange)}
.provider .title .w{color:#fff;position:relative;z-index:2}
.provider .globe{left:0;top:68px;width:183px;height:110px;background:radial-gradient(circle at 62% 58%,#fff6d8 0,#f2b950 10%,#6b5a3a 30%,#22252c 60%,#15171c 100%);z-index:1}
.provider .title{z-index:3}
.provider .squares{z-index:2}
.provider .rule{left:108px;top:54px;width:250px;height:.6px;background:var(--rule)}
.provider .col-right{left:202px;top:60px;width:148px}
.provider .col-left{left:35px;top:183px;width:140px}
.provider .stats{left:198px;top:176px;width:160px;display:flex;justify-content:space-between}
.stat{width:52px;text-align:center}
.stat svg{display:block;margin:0 auto}
.stat-label{font-size:4.3px;color:var(--orange);line-height:1.3;margin-top:1px}

/* landscape spread */
.landscape{left:519px;top:325px;background:linear-gradient(160deg,#e35a1e,var(--orange-deep))}
.landscape .top-rule{left:0;top:12px;width:262px;height:.6px;background:rgba(255,255,255,.7)}
.landscape .vertical{left:38px;top:222px;transform:rotate(-90deg);transform-origin:0 0;color:#fff;font-size:10.5px;letter-spacing:2.2px;white-space:nowrap}
.landscape .growth{left:77px;top:24px;width:106px;height:103px;background:linear-gradient(150deg,#0d2a52,#1d5fa8 55%,#3a9ae0)}
.landscape .intro{left:202px;top:24px;width:114px;color:#fff}
.landscape .sub{font-family:"Open Sans",Arial,sans-serif;font-weight:600;font-size:6.3px;color:#fff}
.landscape .sub-rule{height:.6px;background:rgba(255,255,255,.6);width:106px}
.landscape .feature{color:#fff;font-weight:600;width:108px}

/* structure spread */
.structure{left:135px;top:606px;background:linear-gradient(115deg,#f6f6f6,#e2e2e2)}
.structure .h{color:var(--graphite);font-size:11px}
.structure .rule{height:.6px;background:var(--rule)}
.structure .tablet{left:182px;top:24px;width:152px;height:99px;background:linear-gradient(120deg,#d8c9b2,#8b7d6b 45%,#2d2a28 70%,#b9ad9c)}
.structure .screens{left:32px;top:132px;width:151px;height:99px;background:linear-gradient(120deg,#1a3660,#3f7fc4 50%,#9fc9ee 75%,#c7b2b5)}

/* journey spread */
.journey{left:519px;top:606px;background:var(--dark-page);color:#fff}
.journey .intro{left:45px;top:36px;font-size:5.6px}
.journey .step{position:absolute;left:43px;width:160px}
.journey .step-bar{height:24px;background:#4a4a4a;display:flex;align-items:center;padding-left:7px;font-family:"Montserrat",Arial,sans-serif;font-weight:700;font-size:5.6px;letter-spacing:.8px;text-transform:uppercase}
.journey .step-bar em{font-style:normal;color:var(--orange);margin-left:3px}
.journey .step .body-copy{padding:6px 7px 0;color:#e6e6e6;text-align:left}
.journey .shot{left:204px;width:89px;height:58px}
.journey .accent{left:298px;top:42px;width:3px;height:179px;background:var(--orange)}

/* back cover */
.back{left:338px;top:883px}
.back .top{left:0;top:0;width:358px;height:53px;background:linear-gradient(180deg,#f2f2f2,#dcdcdc)}
.back .wordmark{left:0;width:358px;top:28px;text-align:center;font-size:14px}
.back .doorway{left:0;top:53px;width:358px;height:157px;background:radial-gradient(ellipse 40px 120px at 63% 55%,#f4e6d6 0,#b98d6d 35%,transparent 100%),linear-gradient(90deg,#2a3038,#39414b 50%,#252a30)}
.back .panel{left:31px;top:53px;width:109px;height:157px;background:rgba(225,225,225,.88);padding:27px 8px 0}
.back .panel .h{font-family:"Montserrat",Arial,sans-serif;font-weight:600;font-size:6.6px;color:var(--graphite);line-height:1.15;margin-bottom:6px}
.back .bottom{left:0;top:210px;width:358px;height:44px;background:linear-gradient(180deg,#e8e8e8,#f6f6f6);text-align:center;font-size:4.2px;font-weight:700;color:var(--graphite);padding-top:11px;line-height:1.7}
.back .bottom .o{color:var(--orange)}
</style>
</head>
<body>

<!-- Cover -->
<section class="page cover">
  <div class="abs wordmark">Halcyra</div>
  <div class="abs url-tag">www.halcyra.io</div>
  <div class="photo hero" role="img" aria-label="Glowing network of connected lights over the globe at night"></div>
  <div class="abs heading headline">
    <span class="l1">Change your thinking.</span>
    <span class="l2">Change your approach.</span>
    <span class="l3">Reap the rewards.</span>
  </div>
  <div class="abs cover-rule"></div>
  <div class="abs tagline">Propelling clients through the journey to efficiency.</div>
</section>

<!-- A different provider -->
<section class="page provider">
  <div class="photo globe" role="img" aria-label="Hands holding a glowing digital globe"></div>
  <svg class="abs squares" style="left:10px;top:137px" width="50" height="45" aria-hidden="true">
    <rect x="0" y="5" width="22" height="35" fill="#fff" opacity=".35"/>
    <rect x="18" y="18" width="28" height="27" fill="#fff" opacity=".55"/>
  </svg>
  <div class="abs rule"></div>
  <div class="abs heading title">
    <div class="o">A</div><div class="o">Different</div><div class="o">Provider.</div>
    <div class="w">A different</div><div class="w">type of business</div><div class="w">solution</div>
  </div>
  <div class="abs body-copy col-right">
    <p>is robust, easy to run, straightforward to maintain and effortless to adapt and scale.</p>
    <p>We are different from others in our approach. By listening to our clients and applying our unique methodology, we take stock of the whole environment and challenge the existing way of doing things, streamlining people, process and technology to deliver secure digital business efficiency.</p>
    <p>In providing our clients with an efficient, secure and compliant environment, productivity improvements are recognised, technology spend is optimised and risk is reduced. Services are improved and an enhanced customer experience is delivered to establish competitive advantage in the market.</p>
  </div>
  <div class="abs body-copy col-left">
    <p>We are Halcyra. We have been propelling companies on the journey to automation and efficiency since 2009.</p>
    <p>Our expertise lies in modernising, automating and securing complex technical environments. By balancing compliance with technology, process and people, we establish a clean, compliant and secure business setting for our clients.</p>
  </div>
  <div class="abs stats">
    <div class="stat">
      <svg width="30" height="36" viewBox="0 0 30 36"><circle cx="15" cy="15" r="12" fill="#fff" stroke="#e6e6e6" stroke-width="3.5"/><circle cx="15" cy="15" r="12" fill="none" stroke="#e2531a" stroke-width="3.5" stroke-dasharray="63.3 75.4" transform="rotate(-90 15 15)"/><text x="15" y="17" text-anchor="middle" font-family="Montserrat,sans-serif" font-weight="700" font-size="6.5" fill="#2f2f2f">84%</text><path d="M15 28v6M13 32l2 2 2-2" stroke="#2f2f2f" stroke-width=".7" fill="none"/></svg>
      <div class="stat-label">More efficient<br>IT operations</div>
    </div>
    <div class="stat">
      <svg width="30" height="36" viewBox="0 0 30 36"><circle cx="15" cy="15" r="12" fill="#fff" stroke="#e6e6e6" stroke-width="3.5"/><circle cx="15" cy="15" r="12" fill="none" stroke="#e2531a" stroke-width="3.5" stroke-dasharray="69.4 75.4" transform="rotate(-90 15 15)"/><text x="15" y="17" text-anchor="middle" font-family="Montserrat,sans-serif" font-weight="700" font-size="6.5" fill="#2f2f2f">92%</text><path d="M15 28v6M13 32l2 2 2-2" stroke="#2f2f2f" stroke-width=".7" fill="none"/></svg>
      <div class="stat-label">Increase in speed<br>of execution &amp; delivery</div>
    </div>
    <div class="stat">
      <svg width="30" height="36" viewBox="0 0 30 36"><circle cx="15" cy="15" r="12" fill="#fff" stroke="#e6e6e6" stroke-width="3.5"/><circle cx="15" cy="15" r="12" fill="none" stroke="#e2531a" stroke-width="3.5" stroke-dasharray="45.2 75.4" transform="rotate(-90 15 15)"/><text x="15" y="17" text-anchor="middle" font-family="Montserrat,sans-serif" font-weight="700" font-size="6.5" fill="#2f2f2f">60%</text><path d="M15 28v6M13 32l2 2 2-2" stroke="#2f2f2f" stroke-width=".7" fill="none"/></svg>
      <div class="stat-label">Reduction in costs<br>to the business</div>
    </div>
  </div>
</section>

<!-- The changing landscape -->
<section class="page landscape">
  <div class="abs top-rule"></div>
  <div class="abs heading vertical">The changing landscape</div>
  <div class="photo growth" role="img" aria-label="Business professional with a rising digital growth chart"></div>
  <div class="abs body-copy intro">
    <p>Today's fast-paced business environment is a complex world. Technology and the way people consume information is evolving at speed. Most organisations have evolved over time and often consist of legacy technologies added incrementally, making them hard to adapt and time-consuming to manage.</p>
    <p>These are the environments where Halcyra excels. We streamline and automate the IT estate, securing technology, processes and systems, and propel our clients towards the digital, secure and compliant environment needed for business success.</p>
  </div>
  <div class="abs sub" style="left:77px;top:144px">Digital Efficiency</div>
  <div class="abs sub-rule" style="left:77px;top:155px"></div>
  <div class="abs body-copy feature" style="left:77px;top:168px">An efficient digital environment will establish competitive advantage in this interconnected world. People, process and technology need to be streamlined, and Halcyra are experts in unifying and refining this environment. By merging our unique methodology with market-leading technologies, Halcyra will deliver the digital efficiency that drives your competitive advantage.</div>
  <div class="abs sub" style="left:202px;top:144px">Governance, Risk and Compliance</div>
  <div class="abs sub-rule" style="left:202px;top:155px"></div>
  <div class="abs body-copy feature" style="left:202px;top:168px">Data is often the lifeblood of companies and regulations abound. Making sense of this environment and protecting sensitive information is fundamental. Halcyra can identify your risk profile and pinpoint areas of concern, guiding you in establishing good governance around policy, procedures and technology use.</div>
</section>

<!-- Structuring / propelling -->
<section class="page structure">
  <div class="abs rule" style="left:152px;top:46px;width:30px"></div>
  <div class="abs heading h" style="left:34px;top:25px">Structuring<br>your business<br>in the right way</div>
  <div class="abs body-copy" style="left:34px;top:67px;width:138px">Budgets are tight, technology and security teams need to do more with less, whilst the business requires an ever-increasing array of new technologies to stay ahead. Halcyra provides a holistic wrapper around people, processes and technology to create a more efficient organisation, enabling you to deliver products and services to market faster while enhancing the customer experience.</div>
  <div class="photo tablet" role="img" aria-label="Professional reading a tablet outdoors"></div>
  <div class="photo screens" role="img" aria-label="Person working with floating digital screens"></div>
  <div class="abs rule" style="left:170px;top:158px;width:150px"></div>
  <div class="abs heading h" style="left:195px;top:132px;line-height:1.2">Propelling<br>your technology<br>journey</div>
  <div class="abs body-copy" style="left:195px;top:176px;width:136px">Every organisation is different. Requirements differ, structures contrast and objectives vary. One size does not fit all and an all-encompassing view is essential to start the journey from the correct point. At Halcyra, we consider our client's entire eco-system, understanding usage, technical complexities, process requirements and compliance needs, then redefine the problem to build the solution that will drive your business forward.</div>
</section>

<!-- Ways we work -->
<section class="page journey">
  <div class="abs intro">There are several ways we work with our clients.</div>
  <div class="step" style="top:52px">
    <div class="step-bar">1. Manage the journey <em>for you</em></div>
    <div class="body-copy">Halcyra takes control and full responsibility, so you don't have to worry. We manage the risk. You gain the results and the desired outcome.</div>
  </div>
  <div class="step" style="top:113px">
    <div class="step-bar">2. Go on the journey <em>with you</em></div>
    <div class="body-copy">We work in partnership with you, enhancing your existing team and upskilling your capabilities along the way.</div>
  </div>
  <div class="step" style="top:174px">
    <div class="step-bar">3. The journey is taken <em>by you</em></div>
    <div class="body-copy">Halcyra provide you with the right tools to make the journey yourself.</div>
  </div>
  <div class="photo shot" style="top:42px;background:linear-gradient(135deg,#e7a24a,#6b5a48 45%,#1f2f45)" role="img" aria-label="Hands working at a desk with digital overlay"></div>
  <div class="photo shot" style="top:102px;background:linear-gradient(135deg,#7fb8e6,#2f6fb0 50%,#142c4f)" role="img" aria-label="Team collaborating with holographic screens"></div>
  <div class="photo shot" style="top:163px;background:radial-gradient(circle at 50% 40%,#bfe0ff,#3f7fcf 35%,#0c1a38 75%)" role="img" aria-label="Glowing digital brain above a hand"></div>
  <div class="abs accent"></div>
</section>

<!-- Back cover -->
<section class="page back">
  <div class="abs top"></div>
  <div class="abs wordmark">Halcyra</div>
  <div class="photo doorway" role="img" aria-label="Figure with raised arms standing in a bright doorway"></div>
  <div class="abs panel">
    <div class="h">YOUR<br>PEACE OF MIND<br>IS ESSENTIAL</div>
    <div class="body-copy" style="text-align:left">Building trust and working in partnership with our clients is important to us. Halcyra follows a framework-led, principle-based approach, with a unique methodology based on international quality standard ISO 27001, and has extensive technical expertise across the leading technologies in the market.</div>
  </div>
  <div class="abs bottom">
    Halcyra<br>
    <span class="o">E:</span> info@halcyra.io &nbsp;<span class="o">|</span> <span class="o">W:</span> halcyra.io &nbsp;<span class="o">|</span> <span class="o">T:</span> +44 (0)1632 960418<br>
    Unit 7 | Fernbrook Court | Mill Lane | Ashvale | Surrey | AV4 2QT
  </div>
</section>

</body>
</html>
```